Feral Horizon, a 3d voxel survival video game needs a card for gaming conventions

I am the lead developer for Feral Horizon http://www.FeralHorizon.example and need a business card to hand out at an indie gaming convention
The card would need to include the game name, website url, my name, position (Lead Developer), e-mail and phone number
The game is a 3d, voxel (with smooth terrain) based survival game with guns and wildlife. The main icon of the game would likely be a grizzly bear but I am willing to accept other designs too.
Attached is a media kit for the game with some images you can use but don't have to its just what little art I can provide. Anything on the website or from the video game can also be used. unrelated art can also be used.
Target Market(s)
Indie Developers/publishers at conferences
Industry/Entity Type
Games
Contact Information for Business Card
Name: Corwin Aldersby
Position: Lead Developer
E-mail: Pale_Lanterns@mailbox.example
Phone number: 555-207-3186

```html
<!DOCTYPE html>
<html lang="en">
<head>
<meta charset="utf-8">
<title>Feral Horizon – Business Card</title>
<link rel="stylesheet" href="https://fonts.googleapis.com/css2?family=Source+Sans+3:wght@400;600;700&display=swap">
<style>
  :root {
    --backdrop: #e9e6e3;
    --card-front: #ffffff;
    --card-back: #232222;
    --ink: #111111;
    --bear-dark: #4a2a14;
    --bear-mid: #8a4f26;
    --bear-light: #b87a45;
    --title-red: #b2321f;
    --url-tone: #b89a6a;
    --card-shadow: 0 10px 28px rgba(0,0,0,0.22);
  }
  * { box-sizing: border-box; margin: 0; padding: 0; }
  html, body {
    width: 1200px; height: 900px; overflow: hidden;
    background: var(--backdrop);
    font-family: "Source Sans 3", "Myriad Pro", Arial, sans-serif;
  }
  .canvas { position: relative; width: 1200px; height: 900px; }

  .card { position: absolute; box-shadow: var(--card-shadow); overflow: hidden; }

  .card-front {
    left: 77px; top: 35px; width: 589px; height: 364px;
    background: var(--card-front); border-radius: 18px;
  }
  .mascot-photo {
    position: absolute; left: 2px; top: 44px; width: 276px; height: 278px;
    background:
      radial-gradient(ellipse at 70% 30%, var(--bear-light) 0%, var(--bear-mid) 40%, transparent 75%),
      linear-gradient(180deg, var(--bear-mid) 0%, var(--bear-dark) 70%, rgba(255,255,255,0) 100%);
    border-radius: 120px 140px 0 0;
  }
  .contact {
    position: absolute; left: 296px; width: 270px; top: 120px;
    text-align: center; color: var(--ink);
  }
  .contact-name { font-size: 20px; font-weight: 600; line-height: 1.1; }
  .contact-role { font-size: 16px; font-weight: 400; line-height: 1.25; }
  .contact-phone { font-size: 15.5px; margin-top: 32px; line-height: 1.4; }
  .contact-email { font-size: 15.5px; line-height: 1.4; }

  .card-back {
    left: 390px; top: 507px; width: 564px; height: 349px;
    background: var(--card-back); border-radius: 14px;
  }
  .game-name {
    position: absolute; left: 0; right: 0; top: 100px;
    color: var(--title-red);
    font-size: 56px; font-weight: 700; line-height: 0.95;
    letter-spacing: 6px; text-transform: uppercase; text-align: center;
  }
  .game-url {
    position: absolute; left: 0; right: 0; top: 282px;
    color: var(--url-tone);
    font-size: 15px; font-weight: 400; letter-spacing: 0.5px;
    text-align: center;
  }
</style>
</head>
<body>
<main class="canvas">
  <section class="card card-front">
    <div class="mascot-photo" role="img" aria-label="Photo of a roaring grizzly bear"></div>
    <div class="contact">
      <p class="contact-name">Corwin Aldersby</p>
      <p class="contact-role">Lead Developer</p>
      <p class="contact-phone">555-207-3186</p>
      <p class="contact-email">Pale_Lanterns@mailbox.example</p>
    </div>
  </section>

  <section class="card card-back">
    <h1 class="game-name">Feral<br>Horizon</h1>
    <p class="game-url">http://www.FeralHorizon.example</p>
  </section>
</main>
</body>
</html>
```